Optimising your students' achievement in PLQ English

The flyer is for an audience of English teachers in NSW, who are teaching PLQ English. We need a flyer that provides clear information about the services we can offer in terms of advice and professional learning for English teachers.
We are leading experts in this field and this is the first time we are offering tailored professional learning for individual schools and their English staff.
Attached is a document that provides details of the proposed content and inclusions (logos) for the flyer.

```html
<!DOCTYPE html>
<html lang="en">
<head>
<meta charset="utf-8">
<title>Professional learning for English staff</title>
<link rel="stylesheet" href="https://fonts.googleapis.com/css2?family=Montserrat:wght@300;400;600&display=swap">
<style>
  :root {
    --magenta: #a83563;
    --navy: #1d3a5c;
    --ink: #2b2b2b;
    --rule: #d9d9d9;
    --footer: #dddddd;
    --band: rgba(40, 44, 52, 0.72);
    --white: #ffffff;
  }
  * { box-sizing: border-box; margin: 0; padding: 0; }
  html, body { width: 778px; height: 1200px; overflow: hidden; background: var(--white); }
  body { font-family: "Montserrat", Arial, sans-serif; color: var(--ink); }
  .flyer { position: relative; width: 778px; height: 1200px; overflow: hidden; }

  .hero {
    position: absolute; left: 0; top: 0; width: 778px; height: 400px;
    background: linear-gradient(120deg, #e9e6e1 0%, #cfc6bd 30%, #9b6f6a 55%, #6f7f9a 75%, #3c3f4a 100%);
  }
  .hero-band {
    position: absolute; left: 0; top: 268px; width: 514px; height: 114px;
    background: var(--band);
    padding: 10px 0 0 27px;
  }
  .hero-title {
    font-weight: 300; font-size: 40px; line-height: 48px; color: var(--white);
    letter-spacing: 0.2px;
  }

  .section-heading {
    position: absolute; left: 36px; font-weight: 300; color: var(--magenta);
  }
  .section-rule { position: absolute; left: 0; height: 5px; background: var(--rule); }

  .heading-consultants { top: 424px; font-size: 31px; }
  .rule-consultants { top: 465px; width: 218px; }

  .consultant { position: absolute; top: 494px; }
  .consultant-left { left: 91px; }
  .consultant-right { left: 427px; }
  .affiliation-mark { display: flex; align-items: center; gap: 8px; height: 42px; }
  .affiliation-mark .mark-square { width: 30px; height: 34px; background: var(--navy); }
  .affiliation-mark .mark-name { font-size: 11px; font-weight: 400; color: var(--navy); line-height: 13px; width: 90px; }
  .consultant-name { font-weight: 300; font-size: 20px; line-height: 24px; color: var(--navy); }
  .consultant-left .consultant-name { margin-top: 20px; }
  .consultant-right .consultant-name { margin-top: 44px; }
  .consultant-details { font-size: 12px; line-height: 16px; color: var(--ink); margin-top: 9px; }
  .column-divider { position: absolute; left: 377px; top: 479px; width: 1px; height: 196px; background: #c8c8c8; }

  .heading-support { top: 697px; font-size: 22px; }
  .rule-support { top: 727px; width: 336px; }

  .support-body { position: absolute; left: 38px; top: 752px; width: 690px; font-size: 12.3px; line-height: 15.5px; }
  .support-body p { margin-bottom: 15px; }
  .support-body ul { list-style: none; margin-left: 18px; }
  .support-body li { position: relative; padding-left: 12px; }
  .support-body li::before { content: "•"; position: absolute; left: 0; top: 0; }
  .support-list li { margin-bottom: 15px; }
  .targeted-heading { font-weight: 600; margin: 4px 0 12px; }
  .targeted-list li { margin-bottom: 0; }

  .footer {
    position: absolute; left: 0; top: 1095px; width: 778px; height: 105px;
    background: var(--footer); padding: 14px 38px 0;
    font-size: 11.6px; line-height: 20px;
  }
</style>
</head>
<body>
<main class="flyer">
  <div class="hero" role="img" aria-label="Photo of six smiling senior students standing together beside library bookshelves"></div>
  <div class="hero-band">
    <h1 class="hero-title">Professional learning<br>for English staff</h1>
  </div>

  <h2 class="section-heading heading-consultants">Consultants</h2>
  <div class="section-rule rule-consultants"></div>

  <section class="consultant consultant-left">
    <div class="affiliation-mark"><span class="mark-square"></span><span class="mark-name">Harbourview University</span></div>
    <h3 class="consultant-name">Associate Professor<br>Helena Marsh</h3>
    <p class="consultant-details">Harbourview University<br>Chief Examiner, PLQ English<br>(Standard and Advanced, 2006-2011)</p>
  </section>

  <div class="column-divider"></div>

  <section class="consultant consultant-right">
    <div class="affiliation-mark"><span class="mark-square"></span><span class="mark-name">Harbourview University</span></div>
    <h3 class="consultant-name">Dr Owen Pryce</h3>
    <p class="consultant-details">St Brendan's Catholic University<br>Former Inspector, English at the State Board of<br>Curriculum, Teaching and Educational Standards</p>
  </section>

  <h2 class="section-heading heading-support">How we can support you:</h2>
  <div class="section-rule rule-support"></div>

  <section class="support-body">
    <p>School-based professional learning for Stage 6 English teachers with leading experts in PLQ English and examinations.</p>
    <p>We will work with you and your staff to:</p>
    <ul class="support-list">
      <li>Develop and/or provide advice on all aspects of Stage 6 English programs for optimal student engagement and learning outcomes</li>
      <li>Provide intensive professional learning to assist Stage 6 English teachers in raising students’ achievement in PLQ English examinations (one-off professional learning days tailored to your needs, and/or sustained collaboration with your staff)</li>
    </ul>
    <p class="targeted-heading">Provide targeted programs in:</p>
    <ul class="targeted-list">
      <li>Preparing your students for PLQ English examinations: what they need to know to succeed in English examinations</li>
      <li>Teaching and learning resources specifically focused on building examination technique and confidence</li>
      <li>Successfully planning, programming, teaching and resourcing Stage 6 English</li>
      <li>Research-based strategies and the most effective pedagogy for developing students’ writing abilities in PLQ English examinations</li>
    </ul>
  </section>

  <footer class="footer">
    To discuss your professional learning requirements, or for additional information, please contact Helena (helena.marsh@harbourview.edu.au) or Owen (owen.pryce@stbrendan.edu.au) and we will be happy to talk with you about any aspect of your Stage 6 English teaching.
  </footer>
</main>
</body>
</html>
```